LAW FIRM - RE-DESIGN - (professional, excellence, tradition and innovation)

We are a premier law firm in New South Wales, Australia. We pride ourselves on being cutting edge and up to date in our market.

Our firm formed in 1874 and has a particularly strong tradition within it's geographic footprint. acting for clients over multiple generations. Despite our regional background, our reputation for excellence has enable us to remain highly visible in a large area.

We have invested heavily in ensuring future planning of this business, and do so on a recurring basis. This has lead to a review of our existing web site.

Although serviceable we feel our previous website is out-of-date and not as in touch with the modern market. We are aware that for the emerging clients a web site is often the face of a firm and a failure to hold attention on the first page may fail to capture the client.

We are seeking designs to communicate the core values of professionalism and excellence. At the same time as maintaining traditional country values of honesty, integrity and hard work we strive to embrace changes to the law and technology.

Target Market(s)

Clients of Law Firm

Industry/Entity Type

Law Firm

Coding

Coded - Design and coding required

Number of Pages Required

5+ page

Requirements
Must have
• A strong sense of professionalism and excellence with a careful balance between traditional values and innovation.
Nice to have
• We have included within our design brief links to top competitors sites to assist for design concepts.

```html
<!DOCTYPE html>
<html lang="en">
<head>
<meta charset="utf-8">
<title>Kestrel Law</title>
<link rel="stylesheet" href="https://fonts.googleapis.com/css2?family=Roboto:wght@300;400;500;700&family=Roboto+Condensed:wght@400;700&display=swap">
<style>
  :root {
    --blue: #1e7fd0;
    --blue-bright: #2a8de0;
    --blue-deep: #15569d;
    --navy: #2a3552;
    --navy-dark: #1c2440;
    --city: #3f6aa0;
    --white: #ffffff;
    --ink: #1b2a44;
    --accent: #1b62b8;
    --paper: #f7f8fa;
  }
  * { box-sizing: border-box; margin: 0; padding: 0; }
  html, body { width: 1200px; height: 676px; overflow: hidden; background: var(--white); }
  body { font-family: "Roboto", Arial, sans-serif; color: var(--white); position: relative; }

  .top-bar {
    position: absolute; left: 0; top: 0; width: 1200px; height: 38px;
    background: var(--blue); display: flex; align-items: center;
    padding: 0 40px; font-family: "Roboto Condensed", Arial, sans-serif; font-size: 13px;
  }
  .top-bar .contact-item { display: flex; align-items: center; gap: 7px; margin-right: 30px; }
  .top-bar .learn { margin-left: auto; display: flex; align-items: center; gap: 24px; font-size: 12px; }
  .top-bar .learn strong { font-weight: 700; }

  .hero { position: absolute; left: 0; top: 38px; width: 1200px; height: 512px; overflow: hidden; }
  .hero svg.backdrop { position: absolute; inset: 0; }

  .site-header {
    position: absolute; left: 0; top: 38px; width: 1200px; height: 66px;
    display: flex; align-items: center; padding: 0 40px;
    border-bottom: 1px solid rgba(255,255,255,0.25);
  }
  .brand { display: flex; align-items: center; gap: 10px; font-size: 24px; font-weight: 500; color: var(--white); width: 270px; }
  .brand .mark { width: 16px; height: 16px; background: var(--white); }
  .main-nav { display: flex; gap: 34px; font-family: "Roboto Condensed", Arial, sans-serif; font-size: 15px; }
  .main-nav a { color: var(--white); text-decoration: none; }
  .main-nav a.is-light { color: #dfeaf7; }
  .header-actions { margin-left: auto; display: flex; gap: 10px; font-family: "Roboto Condensed", Arial, sans-serif; font-size: 13px; }
  .btn { border-radius: 16px; padding: 7px 12px; }
  .btn-outline { border: 1px solid var(--white); color: var(--white); }
  .btn-solid { background: var(--white); color: var(--ink); }

  .hero-badge {
    position: absolute; left: 462px; top: 180px; width: 290px; height: 290px; border-radius: 50%;
    background: rgba(255,255,255,0.22);
    display: flex; flex-direction: column; align-items: center; justify-content: center;
    font-family: "Roboto", Arial, sans-serif; line-height: 1.1; text-align: center;
  }
  .hero-badge .line { font-size: 36px; font-weight: 300; letter-spacing: 1px; }
  .hero-badge .strong { font-size: 46px; font-weight: 700; }

  .welcome {
    position: absolute; left: 0; top: 550px; width: 1200px; height: 98px;
    background: linear-gradient(90deg, var(--blue-deep), var(--blue-bright));
    text-align: center; padding-top: 12px;
  }
  .welcome h1 { font-family: "Roboto Condensed", Arial, sans-serif; font-size: 21px; font-weight: 700; }
  .welcome .rule { width: 1040px; margin: 8px auto 10px; border-top: 1px dashed rgba(255,255,255,0.7); }
  .welcome p { font-family: "Roboto Condensed", Arial, sans-serif; font-size: 12.5px; line-height: 1.5; width: 980px; margin: 0 auto; }

  .services { position: absolute; left: 0; top: 648px; width: 1200px; height: 28px; background: var(--paper); text-align: center; }
  .services h2 { font-family: "Roboto Condensed", Arial, sans-serif; font-size: 20px; font-weight: 700; color: var(--ink); padding-top: 2px; }
  .services h2 span { color: var(--accent); }
</style>
</head>
<body>
  <div class="top-bar">
    <span class="contact-item">
      <svg width="12" height="12" viewBox="0 0 24 24"><path fill="#fff" d="M6.6 10.8a15 15 0 0 0 6.6 6.6l2.2-2.2c.3-.3.7-.4 1-.2 1.1.4 2.3.6 3.6.6.6 0 1 .4 1 1V20c0 .6-.4 1-1 1C10.6 21 3 13.4 3 4c0-.6.4-1 1-1h3.5c.6 0 1 .4 1 1 0 1.3.2 2.5.6 3.6.1.3 0 .7-.2 1z"/></svg>
      +1 800 555 01 48
    </span>
    <span class="contact-item">
      <svg width="13" height="10" viewBox="0 0 26 20"><rect x="1" y="1" width="24" height="18" rx="2" fill="#fff"/><path d="M2 3l11 8 11-8" stroke="#1e7fd0" stroke-width="2" fill="none"/></svg>
      info@kestrellaw.com
    </span>
    <div class="learn">
      <strong>Learn More:</strong>
      <span>Our History</span>
      <span>Our Philosophy</span>
      <svg width="12" height="12" viewBox="0 0 24 24"><circle cx="10" cy="10" r="7" stroke="#fff" stroke-width="3" fill="none"/><path d="M15 15l6 6" stroke="#fff" stroke-width="3"/></svg>
    </div>
  </div>

  <div class="hero">
    <svg class="backdrop" width="1200" height="512" viewBox="0 0 1200 512">
      <defs>
        <linearGradient id="cityTone" x1="0" y1="0" x2="0" y2="1">
          <stop offset="0" stop-color="#6d8fbe"/>
          <stop offset="0.5" stop-color="#3e6298"/>
          <stop offset="1" stop-color="#2a4678"/>
        </linearGradient>
        <linearGradient id="columnTone" x1="0" y1="0" x2="1" y2="1">
          <stop offset="0" stop-color="#2d3858"/>
          <stop offset="1" stop-color="#1e2644"/>
        </linearGradient>
      </defs>
      <rect width="1200" height="512" fill="url(#cityTone)" role="img" aria-label="Aerial view of a city skyline at dusk"/>
      <polygon points="0,0 770,0 470,512 0,512" fill="url(#columnTone)" role="img" aria-label="Classical stone columns seen from below"/>
    </svg>
  </div>

  <header class="site-header">
    <div class="brand"><span class="mark"></span>Kestrel Law</div>
    <nav class="main-nav">
      <a href="#">HOME</a>
      <a href="#">ABOUT US</a>
      <a href="#">SERVICES</a>
      <a href="#">OUR PEOPLE</a>
      <a href="#" class="is-light">CONTACT</a>
    </nav>
    <div class="header-actions">
      <span class="btn btn-outline">Log In</span>
      <span class="btn btn-solid">Request a Quote</span>
    </div>
  </header>

  <div class="hero-badge">
    <span class="line">DO YOU</span>
    <span class="strong">NEED</span>
    <span class="line">A</span>
    <span class="line">LAWYER</span>
  </div>

  <section class="welcome">
    <h1>Welcome to Kestrel Law</h1>
    <div class="rule"></div>
    <p>Kestrel Law has been in existence since 1874 originally starting out as the firm Walter Hensley of Glen Arden. In 1894 Walter Hensley was acquired by Colonel RT Marsh. The firm became known as RT Marsh &amp; Co. until early 1970 when it became Marsh &amp; Co, Marsh Ellery &amp; Co in 1979 and Marsh Ellery &amp; Vance in 1982</p>
  </section>

  <section class="services">
    <h2>Our <span>Services</span></h2>
  </section>
</body>
</html>
```